Tolland Imaging
Mobile Ultrasound Solutions
Professional
Helen Marsh
Executive Sales Representative
Alder Falls, Westmark
info@tollandimaging-example.com
tollandimaging-example.com

```html
<!DOCTYPE html>
<html lang="en">
<head>
<meta charset="utf-8">
<title>Tolland Imaging – Business Card</title>
<link rel="stylesheet" href="https://fonts.googleapis.com/css2?family=Open+Sans:ital,wght@0,400;0,700;1,700&display=swap">
<style>
  :root {
    --bg: #2e2e2e;
    --card: #ffffff;
    --brand-blue: #2b3f9e;
    --accent-blue: #2f56c9;
    --deep-blue: #1f3aa8;
    --swoosh-grey: #c9ccd3;
    --text-dark: #1d1d1f;
    --text-body: #333333;
    --divider: #e2e2e2;
  }
  * { box-sizing: border-box; margin: 0; padding: 0; }
  html, body {
    width: 1200px;
    height: 780px;
    overflow: hidden;
    background: var(--bg);
    font-family: "Open Sans", Arial, sans-serif;
  }
  .business-card {
    position: absolute;
    left: 100px;
    top: 105px;
    width: 1000px;
    height: 570px;
    background: var(--card);
    border-radius: 30px;
    overflow: hidden;
  }
  .brand {
    position: absolute;
    left: 0;
    top: 0;
    width: 370px;
    height: 430px;
    display: flex;
    flex-direction: column;
    align-items: center;
    justify-content: center;
    gap: 22px;
  }
  .brand-mark {
    width: 120px;
    height: 120px;
    border-radius: 50%;
    background: var(--accent-blue);
  }
  .brand-name {
    font-weight: 700;
    font-size: 34px;
    color: var(--brand-blue);
    letter-spacing: 0.5px;
  }
  .divider {
    position: absolute;
    left: 370px;
    top: 0;
    width: 2px;
    height: 420px;
    background: linear-gradient(to bottom, var(--divider), rgba(226,226,226,0));
  }
  .contact {
    position: absolute;
    left: 400px;
    top: 50px;
    color: var(--text-body);
  }
  .person-name {
    font-weight: 700;
    font-size: 31px;
    color: var(--brand-blue);
    line-height: 1.1;
  }
  .person-title {
    font-weight: 700;
    font-style: italic;
    font-size: 19px;
    color: var(--text-dark);
    margin-top: 4px;
  }
  .contact-list {
    list-style: none;
    margin-top: 40px;
    font-size: 18px;
  }
  .contact-list li {
    display: flex;
    align-items: center;
    gap: 12px;
    height: 30px;
    white-space: nowrap;
  }
  .contact-list li.location { margin-bottom: 34px; }
  .contact-list svg { width: 18px; height: 18px; flex: none; }
  .swoosh {
    position: absolute;
    left: 0;
    bottom: 0;
    width: 1000px;
    height: 190px;
  }
</style>
</head>
<body>
  <main class="business-card">
    <div class="brand">
      <div class="brand-mark"></div>
      <div class="brand-name">Tolland Imaging</div>
    </div>

    <div class="divider"></div>

    <section class="contact">
      <h1 class="person-name">Helen Marsh</h1>
      <p class="person-title">Executive Sales Representative</p>
      <ul class="contact-list">
        <li class="location">
          <svg viewBox="0 0 20 20"><path d="M10 2 L19 10 H16 V18 H12 V13 H8 V18 H4 V10 H1 Z" fill="var(--deep-blue)"/></svg>
          Alder Falls, Westmark
        </li>
        <li class="phone">
          <svg viewBox="0 0 20 20"><path d="M5 2 C3 3 2 5 3 8 C5 13 8 16 12 18 C15 19 17 18 18 16 L14 12 L12 14 C10 13 8 11 7 9 L9 7 Z" fill="var(--deep-blue)"/></svg>
          555-014-7290
        </li>
        <li class="email">
          <svg viewBox="0 0 20 20"><circle cx="10" cy="10" r="8" fill="none" stroke="var(--deep-blue)" stroke-width="2"/><circle cx="10" cy="10" r="3" fill="none" stroke="var(--deep-blue)" stroke-width="2"/></svg>
          info@tollandimaging-example.com
        </li>
        <li class="website">
          <svg viewBox="0 0 20 20"><circle cx="10" cy="10" r="8.5" fill="var(--deep-blue)"/><path d="M2 10 H18 M10 1.5 C6 5 6 15 10 18.5 M10 1.5 C14 5 14 15 10 18.5" fill="none" stroke="#fff" stroke-width="1"/></svg>
          www.tollandimaging-example.com
        </li>
      </ul>
    </section>

    <svg class="swoosh" viewBox="0 0 1000 190" preserveAspectRatio="none" aria-hidden="true">
      <defs>
        <linearGradient id="blueBand" x1="0" y1="0" x2="1" y2="0">
          <stop offset="0" stop-color="#3a63d6"/>
          <stop offset="1" stop-color="#1c34a0"/>
        </linearGradient>
      </defs>
      <path d="M0 120 C300 150 650 130 1000 40 L1000 190 L0 190 Z" fill="var(--swoosh-grey)"/>
      <path d="M0 150 C320 175 680 150 1000 70 L1000 190 L0 190 Z" fill="url(#blueBand)"/>
    </svg>
  </main>
</body>
</html>
```